Design a New Tennis and Athletic Club- Business cards desired with a wow factor.

Help us find a exciting and useful design for our business.
1. Design should be two-sided made of materials that will last.
2. Eye-popping graphics
3. Space for changeable quotes on the back of our card with our "wolf" program logo.
4. Recolor wolf to match club colors

Target Market(s)

Players parents coaches clients

Industry/Entity Type

Business

Contact Information for Business Card

Birchwood Paddle + Wellness
Derek Hollins
Director of Tennis Operations
2817 Meadowcrest Ave NE
Grand Rapids Michigan 49318
Office (616) 555-0142
Cell (269) 555-0186
Email dhollins482@mailbox-example.com
Website http://www.bwpaddle-example.com
Facebook https://www.facebook.com/BWPaddleExample

Font styles to use
Serif

Colors
0555a3
f37122
ffffff

Requirements
Must have
• 1.interesting contemporary design,
• 2. 2 sided
• 3. ability to swap out staff information for other trainers and professionals
Nice to have
• 1.Space for changeable quotes on the back of the card
• 2. change wolf logo body to match club color blue
• 3. some white space on card for notes to be written.
Should not have
• boring same old consruction

```html
<!DOCTYPE html>
<html lang="en">
<head>
<meta charset="utf-8">
<title>Birchwood Paddle + Wellness – Business Card</title>
<link rel="stylesheet" href="https://fonts.googleapis.com/css2?family=Montserrat:wght@400;500;700;800&display=swap">
<style>
  :root {
    --club-blue: #0555a3;
    --club-orange: #f37122;
    --white: #ffffff;
    --card-white: #f4f3f8;
    --navy: #151c3a;
    --stage: #e9e7e3;
  }
  * { box-sizing: border-box; margin: 0; padding: 0; }
  html, body {
    width: 1200px; height: 800px; overflow: hidden;
    background: var(--stage);
    font-family: "Montserrat", sans-serif;
  }
  .card {
    position: absolute;
    top: 246px;
    width: 540px; height: 308px;
    border-radius: 4px;
    box-shadow: 0 6px 18px rgba(0,0,0,.12);
    overflow: hidden;
  }
  /* Front side: program mark */
  .card--front { left: 40px; background: var(--card-white); }
  .program-art {
    position: absolute; left: 170px; top: 38px;
    width: 200px; height: 110px; border-radius: 8px;
    background: linear-gradient(160deg, #2d2f6b, #141a3a);
  }
  .program-mark {
    position: absolute; left: 0; right: 0; top: 160px;
    text-align: center;
    font-weight: 800; font-size: 38px; letter-spacing: 1px;
    color: var(--navy); text-transform: uppercase; line-height: 1;
  }
  .social {
    position: absolute; right: 30px; top: 200px; display: flex; gap: 8px;
  }
  .social span {
    width: 24px; height: 24px; border-radius: 50%; background: var(--club-orange);
  }
  .front-rule {
    position: absolute; left: 210px; right: 90px; top: 230px;
    height: 2px; background: var(--navy);
  }
  .tag {
    position: absolute; display: flex; align-items: center;
    background: var(--navy);
    clip-path: polygon(0 0, calc(100% - 14px) 0, 100% 50%, calc(100% - 14px) 100%, 0 100%);
  }
  .tag--handle {
    left: 14px; top: 244px; height: 34px; padding: 0 26px 0 14px;
    color: var(--white); font-weight: 500; font-size: 16px; border-radius: 4px 0 0 4px;
  }
  /* Back side: staff details */
  .card--back { left: 620px; background: var(--club-blue); color: var(--white); }
  .staff-name {
    position: absolute; left: 30px; top: 30px;
    font-weight: 800; font-size: 30px; line-height: 1;
  }
  .staff-name .surname { color: var(--club-orange); }
  .staff-title {
    position: absolute; left: 30px; top: 68px;
    font-size: 15px; font-weight: 400;
  }
  .contact-list {
    position: absolute; left: 30px; top: 118px; list-style: none;
    font-size: 14px; line-height: 24px;
  }
  .contact-list li { display: flex; align-items: center; gap: 10px; }
  .contact-list svg { width: 14px; height: 14px; fill: var(--club-orange); flex: none; }
  .club-mark {
    position: absolute; right: 28px; top: 40px; width: 170px;
    display: flex; align-items: center; gap: 10px;
    color: var(--navy); font-weight: 700; font-size: 17px; line-height: 1.2;
  }
  .club-mark::before {
    content: ""; width: 30px; height: 30px; flex: none;
    border-radius: 50%; background: var(--navy);
  }
  .tag--club {
    left: 0; top: 200px; height: 38px; padding: 0 34px 0 30px;
    color: var(--club-orange); font-size: 15px; font-weight: 500;
  }
  .address {
    position: absolute; right: 30px; top: 196px; text-align: right;
    font-size: 14px; line-height: 22px;
  }
  .back-rule {
    position: absolute; right: 30px; top: 272px; width: 220px;
    height: 2px; background: var(--navy);
  }
</style>
</head>
<body>
  <section class="card card--front" aria-label="Card front">
    <div class="program-art" role="img" aria-label="Wolf mascot illustration in club blue and orange"></div>
    <div class="program-mark">Ridgeline Tennis</div>
    <div class="social" aria-label="Social media links"><span></span><span></span></div>
    <div class="front-rule"></div>
    <div class="tag tag--handle">BWPaddle</div>
  </section>

  <section class="card card--back" aria-label="Card back">
    <h1 class="staff-name">Derek <span class="surname">Hollins</span></h1>
    <p class="staff-title">Director of Tennis Operations</p>
    <ul class="contact-list">
      <li><svg viewBox="0 0 24 24"><path d="M6.6 10.8a15 15 0 0 0 6.6 6.6l2.2-2.2a1 1 0 0 1 1-.25 11.4 11.4 0 0 0 3.6.6 1 1 0 0 1 1 1V20a1 1 0 0 1-1 1A17 17 0 0 1 3 4a1 1 0 0 1 1-1h3.5a1 1 0 0 1 1 1c0 1.25.2 2.45.6 3.6a1 1 0 0 1-.25 1z"/></svg>(616) 555-0142</li>
      <li><svg viewBox="0 0 24 24"><path d="M7 1h10a2 2 0 0 1 2 2v18a2 2 0 0 1-2 2H7a2 2 0 0 1-2-2V3a2 2 0 0 1 2-2zm0 3v14h10V4zm5 15.5a1 1 0 1 0 0 2 1 1 0 0 0 0-2z"/></svg>(269) 555-0186</li>
      <li><svg viewBox="0 0 24 24"><path d="M2 5h20v14H2zm2 2v.5l8 5 8-5V7l-8 5z"/></svg>dhollins482@mailbox-example.com</li>
    </ul>
    <div class="club-mark">Birchwood Paddle + Wellness</div>
    <div class="tag tag--club">Birchwood Paddle + Wellness</div>
    <address class="address" style="font-style:normal">
      www.bwpaddle-example.com<br>
      2817 Meadowcrest Ave NE<br>
      Grand Rapids Michigan 49318
    </address>
    <div class="back-rule"></div>
  </section>
</body>
</html>
```